QTN mobile detailing

Im starting a mobile detailing company where I go to the clients looking for something that will get good attention and looks professional but also resemble what we do.

It Company

```html
<!DOCTYPE html>
<html lang="en">
<head>
<meta charset="utf-8">
<title>QTN mobile detailing – business cards</title>
<link rel="stylesheet" href="https://fonts.googleapis.com/css2?family=Comfortaa:wght@400;700&family=Open+Sans:wght@400&display=swap">
<style>
  :root {
    --page-bg: #ffffff;
    --card-dark: #1c1c1c;
    --card-mid: #3a3a38;
    --card-light: #5a5955;
    --footer-bg: #151515;
    --accent: #f47c0f;
    --accent-soft: rgba(244,124,15,0.55);
    --accent-clear: rgba(244,124,15,0);
    --text-light: #ffffff;
    --text-muted: #e6e6e6;
  }
  * { box-sizing: border-box; margin: 0; padding: 0; }
  html, body {
    width: 1200px; height: 811px; overflow: hidden;
    background: var(--page-bg);
  }
  .canvas { position: relative; width: 1200px; height: 811px; }

  .card {
    position: absolute;
    overflow: hidden;
    background: linear-gradient(160deg, var(--card-dark) 0%, var(--card-mid) 55%, var(--card-light) 75%, var(--card-dark) 100%);
    box-shadow: 0 8px 24px rgba(0,0,0,0.25);
    font-family: "Comfortaa", sans-serif;
    color: var(--text-light);
  }

  .brand { position: absolute; line-height: 1; }
  .brand-name { display: block; font-size: 44px; font-weight: 400; color: var(--text-light); }
  .brand-line { display: block; font-size: 21px; font-weight: 400; color: var(--text-light); margin-top: 2px; }

  .tagline-band {
    position: absolute; left: 0; right: 0;
    background: var(--accent);
    color: var(--text-light);
    font-size: 20px;
    display: flex; align-items: center; justify-content: center;
  }

  .footer {
    position: absolute; left: 0; right: 0; bottom: 0;
    background: var(--footer-bg);
    font-family: "Open Sans", sans-serif;
    font-size: 17px;
    color: var(--text-muted);
  }
  .footer .phone, .footer .email { position: absolute; white-space: nowrap; }

  /* Owner card */
  .card-owner { left: 460px; top: 30px; width: 700px; height: 360px; }
  .card-owner .brand { left: 32px; top: 30px; }
  .owner { position: absolute; right: 44px; top: 36px; text-align: right; color: var(--accent); }
  .owner-name { font-size: 32px; font-weight: 400; }
  .owner-role { font-size: 20px; margin-top: 6px; }
  .accent-flare {
    position: absolute; right: 0; top: 130px; width: 220px; height: 116px;
    background: radial-gradient(ellipse 70% 80% at 85% 100%, var(--accent-soft) 0%, var(--accent-clear) 100%);
  }
  .services { position: absolute; left: 32px; top: 140px; list-style: none; font-size: 14px; line-height: 24px; }
  .services li { display: flex; align-items: center; gap: 8px; }
  .services svg { width: 8px; height: 10px; }
  .card-owner .tagline-band { top: 246px; height: 36px; font-size: 21px; }
  .card-owner .footer { height: 78px; }
  .card-owner .email { right: 40px; top: 8px; }
  .card-owner .phone { left: 34px; bottom: 14px; }

  /* Brand card */
  .card-brand { left: 20px; top: 420px; width: 645px; height: 360px; }
  .card-brand .brand { left: 20px; top: 22px; }
  .side-tab {
    position: absolute; left: 0; top: 118px; width: 30px; height: 96px;
    background: var(--accent); border-radius: 0 8px 8px 0;
  }
  .card-brand .tagline-band { top: 148px; height: 32px; }
  .card-brand .footer { height: 54px; border-top: 6px solid var(--accent); }
  .card-brand .phone { left: 34px; top: 50%; transform: translateY(-50%); }
  .card-brand .email { right: 34px; top: 50%; transform: translateY(-50%); }
</style>
</head>
<body>
<div class="canvas">

  <section class="card card-owner" aria-label="Owner card">
    <div class="brand">
      <span class="brand-name">QTN</span>
      <span class="brand-line">mobile detailing</span>
    </div>
    <div class="owner">
      <p class="owner-name">Marco Delgado</p>
      <p class="owner-role">Owner / operator</p>
    </div>
    <div class="accent-flare" role="img" aria-label="Orange rising arrows accent"></div>
    <ul class="services">
      <li><svg viewBox="0 0 8 10"><path d="M1 1 L6 5 L1 9" fill="none" stroke="#f47c0f" stroke-width="2"/></svg>Complete interior detailing</li>
      <li><svg viewBox="0 0 8 10"><path d="M1 1 L6 5 L1 9" fill="none" stroke="#f47c0f" stroke-width="2"/></svg>carpet dyeing</li>
      <li><svg viewBox="0 0 8 10"><path d="M1 1 L6 5 L1 9" fill="none" stroke="#f47c0f" stroke-width="2"/></svg>exterior washing</li>
      <li><svg viewBox="0 0 8 10"><path d="M1 1 L6 5 L1 9" fill="none" stroke="#f47c0f" stroke-width="2"/></svg>waxing paint sealing</li>
    </ul>
    <div class="tagline-band">A detailing service where we come to you</div>
    <div class="footer">
      <span class="email">e.mail:&nbsp; the E-mail</span>
      <span class="phone">tel.: (0) 555-201-7734</span>
    </div>
  </section>

  <section class="card card-brand" aria-label="Brand card">
    <div class="brand">
      <span class="brand-name">QTN</span>
      <span class="brand-line">mobile detailing</span>
    </div>
    <div class="side-tab"></div>
    <div class="tagline-band">A detailing service where we come to you</div>
    <div class="footer">
      <span class="phone">tel.: (0) 555-201-7734</span>
      <span class="email">e.mail:&nbsp; the E-mail</span>
    </div>
  </section>

</div>
</body>
</html>
```